Tallow Roost Lead Generator + Checklist

I have typed up a 9 page word doc to be a lead generator for my website called "6 Simple Secrets Gala Hosts Love" and I am looking for someone to clean it up, and make it professional and inline with our brand.

Logo Hex: #971F20

Industry/Entity Type

Event Planning

Font styles to use
Other font styles liked:
• Helvetica Neue is our brands font, but it doesn't have to be that. Something similar that is rounded would be good like Arial I think.

Requirements
Must have
• Clean, but elegant design.
• Because it is very text heavy, have the topics easily broken out and maybe staggered so that it is easy to identify main topics and sub topics.
Should not have
• Not just looking for basic formating around the edges of the document, but to also have the text displayed in an easily readable way with clear sections.

```html
<!DOCTYPE html>
<html lang="en">
<head>
<meta charset="utf-8">
<title>Tallow Roost – 6 Simple Secrets Gala Hosts Love</title>
<link href="https://fonts.googleapis.com/css2?family=Arimo:wght@400;700&family=Dancing+Script:wght@600&display=swap" rel="stylesheet">
<style>
:root{
  --brand:#971F20;
  --brand-dark:#7d1718;
  --ink:#333;
  --paper:#fff;
  --bg:#fff;
}
*{box-sizing:border-box;margin:0;padding:0}
html,body{width:1200px;height:515px;overflow:hidden;background:var(--bg)}
body{position:relative;font-family:Arimo,Arial,sans-serif;color:var(--ink)}
.page{position:absolute;width:200px;height:228px;background:var(--paper);overflow:hidden}
.row-top{top:20px}
.row-bottom{top:283px}
.page-header{position:absolute;left:0;top:0;width:200px;height:34px}
.header-wave{position:absolute;left:0;top:0;width:200px;height:34px}
.brand-name{position:absolute;right:20px;top:6px;font-family:Arimo,Arial,sans-serif;font-weight:700;color:var(--brand);font-size:6.5px;line-height:1;white-space:nowrap;display:flex;align-items:center;gap:2px}
.brand-name .mark{width:5px;height:5px;background:var(--brand);display:inline-block}
.page-body{position:absolute;left:20px;right:18px;top:38px;font-size:2.75px;line-height:1.38}
.page-body p{margin-bottom:2.4px}
.page-body ol{margin:0 0 2.4px 5px}
.page-body .indent{text-indent:6px}
.script-title{font-family:"Dancing Script",cursive;color:var(--brand);text-align:center;font-size:4.6px;line-height:1.1;margin-bottom:4px}
.section{font-family:"Dancing Script",cursive;color:var(--brand);text-decoration:underline;font-size:4.4px;margin:3px 0 2.5px}
.tip b{color:var(--brand)}
.tip b::before{content:"★ ";}
.page-number{position:absolute;bottom:9px;left:0;right:0;text-align:center;font-size:2.6px}
.corner-name{position:absolute;right:18px;bottom:6px;font-size:4px;font-weight:700;color:var(--brand)}
.checklist h4{font-size:2.8px;font-weight:700;margin:3px 0 0.5px}
.checklist ul{list-style:none;margin-left:5px}
.checklist li::before{content:"○ ";}
.cover{position:absolute;top:20px;width:180px;height:236px;background:var(--paper);overflow:hidden}
.cover-front{left:11px}
.cover-back{left:1009px}
.cover-logo{position:absolute;font-weight:700;color:var(--brand);font-size:15px;line-height:1;display:flex;align-items:center;gap:5px;white-space:nowrap}
.cover-logo .mark{width:12px;height:12px;background:var(--brand)}
.cover-title{position:absolute;left:0;right:0;top:115px;text-align:center;font-family:"Dancing Script",cursive;color:var(--brand);font-size:8.6px;line-height:1.15}
.cover-band{position:absolute;left:0;width:180px}
</style>
</head>
<body>

<!-- Front cover -->
<section class="cover cover-front">
  <div class="cover-logo" style="left:47px;top:50px"><span class="mark"></span>Tallow Roost</div>
  <h1 class="cover-title">6 Simple Secrets Gala Hosts Love<br>(and how to use them!)</h1>
  <svg class="cover-band" style="top:160px" width="180" height="76" viewBox="0 0 180 76" aria-hidden="true">
    <path d="M0 18 C50 30 110 -2 180 8 L180 76 L0 76 Z" fill="var(--brand)"/>
    <path d="M0 14 C55 26 115 -6 180 4" fill="none" stroke="var(--brand)" stroke-width="0.6"/>
  </svg>
</section>

<!-- Shared header wave -->
<svg width="0" height="0" style="position:absolute">
  <defs>
    <symbol id="wave" viewBox="0 0 200 34">
      <path d="M0 30 C50 16 110 30 200 6 C120 34 55 22 0 32 Z" fill="var(--brand)"/>
      <path d="M4 27 C60 12 120 24 196 3" fill="none" stroke="var(--brand)" stroke-width="0.4"/>
    </symbol>
  </defs>
</svg>

<!-- Page 1 -->
<article class="page row-top" style="left:212px">
  <header class="page-header"><svg class="header-wave"><use href="#wave"/></svg><div class="brand-name"><span class="mark"></span>Tallow Roost</div></header>
  <div class="page-body">
    <h2 class="script-title">6 Simple Secrets Gala Hosts Love<br>(and how to use them!)</h2>
    <p>You already have enough on your plate.</p>
    <p>The last thing you need is to waste time chasing down basic details from venues to try and present options to your boss, planning team or board. You could just go to the same place you always go to, but that gets old and you'd like to try something new.</p>
    <p>It seemed so easy, but a week goes by and you still don't have good options because some venues still haven't returned your calls and many of the venue websites lack basic details like capacity, pricing and other key policies.</p>
    <p>You consider just driving to the venues to get the information, but who has five extra hours to do that? You definitely don't.</p>
    <p>Don't worry, you're not alone. After planning many local events and going back and forth with venues, I thought there had to be a better way. That's why I created Tallow Roost and put together this guide with the help of other local leaders who have planned events in Cedar Falls.</p>
    <h3 class="script-title" style="text-decoration:underline">Here are the common mistakes we'll go over, and how to avoid them<br>so you'll host an event people will talk about for years.</h3>
    <ol>
      <li>As simple as it sounds, many planners don't start by first thinking about the type of event they are planning.</li>
      <li>Often they don't fully consider the expectations of their audience.</li>
      <li>Planners assume the policies from one venue to the next are similar, when in reality they differ.</li>
      <li>They forget that just like your car runs on gas, your event runs on great food and drinks.</li>
      <li>Lastly, they don't track and ensure the details are completed.</li>
    </ol>
    <h3 class="script-title" style="text-decoration:underline">Here are the 6 simple secrets to avoid these mistakes.</h3>
    <h4 class="section">1. Know the type of event you're planning</h4>
    <p class="indent">a. People who start planning an event without taking the time to think about the type of event they're planning often run into problems.</p>
  </div>
  <div class="page-number">1</div><div class="corner-name">TR</div>
</article>

<!-- Page 2 -->
<article class="page row-top" style="left:412px">
  <header class="page-header"><svg class="header-wave"><use href="#wave"/></svg><div class="brand-name"><span class="mark"></span>Tallow Roost</div></header>
  <div class="page-body">
    <p>For example, if you are planning a one time event and you aren't regularly reaching out to your attendees and actively getting the word out about the event, attendance will be low. If it is a recurring weekly event on the other hand, that level of contact probably isn't needed as people will already be used to coming.</p>
    <p>I recently went to a one-time event and after registering didn't hear anything from the organizer, even on the day of the event! As an attendee I started to wonder if the event was still happening, what to wear and which room to go to once I got to the venue. These are not the kind of thoughts you want running through your guests' heads before the event, you want them excited and looking forward to it.</p>
    <p>This might seem obvious, but it's amazing how often this simple step gets overlooked. It matters because the priorities and steps for a recurring weekly networking event will be much different than a big end of year event.</p>
    <p class="indent">b. By knowing up front the type of event you're planning, you'll start looking at venues that are a great fit and make sure you take the needed steps to host a great event!</p>
    <h4 class="section">2. Know your audience</h4>
    <p class="indent">a. What do they expect?</p>
    <p>The first event I ever planned was for 100 people for my unit and my boss had just been switched out. I made the false assumption that my new boss would like the same venue my previous boss did, and I couldn't have been more wrong. Although I had done everything "right", the venue was much more casual than what he had wanted. So this is why after knowing your event, make sure you know your audience: your boss, board and/or attendees expectations for the event.</p>
    <p>1. Are they looking to make a splash that they hope will propel the group to the next level or are they looking for a practical venue for a recurring event?</p>
    <p>2. Are they looking for an upscale venue where the price is secondary or are they on a tight budget and looking for good value?</p>
    <p>3. Clarifying these expectations up front will ensure you only spend time looking at venues that are a good fit, as opposed to wasting time looking at venues that aren't.</p>
  </div>
  <div class="page-number">2</div><div class="corner-name">TR</div>
</article>

<!-- Page 3 -->
<article class="page row-top" style="left:611px">
  <header class="page-header"><svg class="header-wave"><use href="#wave"/></svg><div class="brand-name"><span class="mark"></span>Tallow Roost</div></header>
  <div class="page-body">
    <p class="indent">b. How many people are expected to come?</p>
    <p>Headcounts are always tricky, but starting to look at venues without a clear idea of how many guests will be coming will also lead you to waste time looking at the wrong size venues. Right or wrong, people judge an event on how well it fills a room. If the hall is half full, people will question if it is even worth being there. But if a room is so small that people can't get in, they won't stick around for long. So finding the right size is key.</p>
    <p>Here are some ideas to get an accurate headcount (especially if this is a first time event).</p>
    <p>1. Attempt to find information about the number of attendees for previous similar events.</p>
    <p>2. Contact people who previously planned the event if this is your first time.</p>
    <p>3. Survey a few people who may be going to see if there is another conflict that will be pulling potential guests away from the event.</p>
    <p>4. You can also create an event page, send out a simple online form or send RSVP emails using an invitation service to get a good headcount as well.</p>
    <p class="indent">c. Now that you have a good feel for the type of event and the headcount the fun part can begin, you can start looking for a venue. By knowing this up front, you'll save yourself the time of going through the process of booking a venue only to find out that it isn't the right size.</p>
    <h4 class="section">3. Ask the venue the right questions</h4>
    <p class="indent">a. Now that you're at a good starting point, it doesn't take long to realize that's only half the battle when planning an event. The next challenge is finding a venue. Sadly, many venues for mid size groups of 20-200 people, such as restaurants, have limited information on their website. Trying to call or email a venue is always a mixed bag, some will get back to you soon, others may take days and some you may never hear back from.</p>
    <p class="tip"><b>Getting Started</b> - Instead of trying to chase down basic details on venue websites and by contacting them, an easy way to start your search is to use our website which will help you quickly eliminate venues that don't meet the basic criteria. You can then save the venues you like, and lastly compare a few that you think would be perfect for your event.</p>
    <p class="tip"><b>360 Tours</b> - One feature that many people find helpful in finding a venue that meets their needs is using the 360 Tour feature found at the bottom of most venue pages.</p>
  </div>
  <div class="page-number">3</div><div class="corner-name">TR</div>
</article>

<!-- Page 4 -->
<article class="page row-top" style="left:802px">
  <header class="page-header"><svg class="header-wave"><use href="#wave"/></svg><div class="brand-name"><span class="mark"></span>Tallow Roost</div></header>
  <div class="page-body">
    <p>The 360 Tours also make it easy for you to give your boss a tour of the venue without even leaving the office.</p>
    <p class="tip"><b>Tech Support</b> - Make sure to check to see if the venue has the tech support and amenities you need, or come up with a plan to provide them internally. It is also good to know how much tech support will cost early in the decision process, because that is a key area where costs can creep up on you.</p>
    <p class="tip"><b>Confirm Fees</b> - Now that you have a few venues in mind, you want to confirm key details like what fees, charges and taxes will apply to get a better picture of the total cost. This can be done by viewing menus and policies attached at the bottom of each venue's page and then messaging the venues to clarify any remaining questions.</p>
    <p class="tip"><b>Refund Policies</b> - Clarify up front when and if there is a deposit due, when payments are due and what the cancellation policy is. This will save you a lot of heartache if there is bad weather, or something unexpected happens with your group and you have to negotiate a refund, where if you know up front there won't be any questions.</p>
    <p class="tip"><b>Parking</b> - This is one of those classic ankle-biter issues that can be frustrating. Make sure to get a good idea from the venue on what parking options will be available, if the venue provides free parking for events, and how the day of week and time of day will affect available parking during the event.</p>
    <p class="tip"><b>Take Notes</b> - Lastly, write all this information in one place and save or tag emails in a way they can be easily found. If you don't you will quickly end up with a mountain of random sticky notes from calls, emails spread out over many places and half-finished shared docs or slide decks.</p>
    <p class="indent">b. Although it is more work up front to ask the right questions, it will be well worth your time and money. There is nothing worse than deciding on a venue, making a deposit, and then to only realize later that the parking options are a deal breaker or something you thought you agreed to ended up being a miscommunication and now you're arguing about getting a deposit back and scrambling at the last minute to find a new venue.</p>
    <h4 class="section">4. Plan the food and drinks - that's why everyone is coming in the first place</h4>
    <p class="indent">a. We've all been to those events where there isn't enough food, or the food is cold and the drinks are warm - you definitely don't want to be planning the event where people leave early to go to a drive through on the way home.</p>
  </div>
  <div class="page-number">4</div><div class="corner-name">TR</div>
</article>

<!-- Page 5 -->
<article class="page row-bottom" style="left:212px">
  <header class="page-header"><svg class="header-wave"><use href="#wave"/></svg><div class="brand-name"><span class="mark"></span>Tallow Roost</div></header>
  <div class="page-body">
    <p class="tip"><b>Have a Plan</b> - Have basic questions answered such as what food will be served, when will it be served or how can it be ordered, if there will be a private bar just for your group or if guests need to go to a public bar.</p>
    <p class="tip"><b>Caterer Coordination</b> - All of this is even more important if you have a caterer or are bringing in outside food which typically requires a higher level of coordination than if the venue provides the food. Also, before you start looking into outside caterers or bringing your own food, make sure you check with the venue to see what their requirements are. Many venues have a short list of caterers they allow or require certain paperwork.</p>
    <p class="indent">b. Ensuring that the food and drink details are nailed down is a must. After all, if everyone is having a good time, some other minor details that may have been missed will probably be quickly forgotten by the next day. On the other hand, if people aren't having a good time, they are only going to remember problems more clearly!</p>
    <h4 class="section">5. Lastly, Don't take anything for granted</h4>
    <p class="indent">a. Even after the heavy lifting is done and you've found your venue and have any needed vendors lined up, don't just kick back and wait for the event to happen. Remember, great events don't just happen - they happen because the planner commits to planning a great event.</p>
    <p class="tip"><b>Confirm Venue and Vendors</b> - Depending on the size of the event, make sure to follow up with the venue and vendors about a month ahead, a week ahead and the day before to make sure that everything is set, and no unexpected issues have come up at the last minute (vendors being sick, running out of supplies, etc) that may derail the event.</p>
    <p class="tip"><b>Communicate with Guests</b> - Guests can often require a similar level of detail. Sending out a reminder with basic details a week before and the day before is a good way to reduce no-shows and last minute calls and texts from people at the venue who can't find the room, parking, etc. Event tools make this a breeze.</p>
    <p class="tip"><b>Signage</b> - Clear and simple signs on the day of an event are usually great for any venue, especially if they have multiple rooms or the private event room is on a different floor or in the back of the venue.</p>
    <p class="tip"><b>"Day of" Box</b> - Again, it depends on the type and size of the event, but it is good to start collecting everything you'll need for the event a day or two beforehand in one place. Programs, Signs, Easels, Pens, Nametags, Wireless slide advancers, Speaker gifts, Scripts, Adapter cables for laptops and projectors, etc so that when the time comes you can easily ensure everything is in one place and it will give you time to run to the store the day before the event, as opposed to realizing you're missing something during setup on the day of the event.</p>
  </div>
  <div class="page-number">5</div><div class="corner-name">TR</div>
</article>

<!-- Page 6 -->
<article class="page row-bottom" style="left:412px">
  <header class="page-header"><svg class="header-wave"><use href="#wave"/></svg><div class="brand-name"><span class="mark"></span>Tallow Roost</div></header>
  <div class="page-body">
    <p class="tip"><b>"Day of" Checklist</b> - If the event isn't an event you do every week, I'd highly recommend developing a simple 'day of' checklist that covers everything you need to do, everything you need to bring, etc. for the day of the event. There is simply too much going on to remember everything, and especially if something unexpected happens - it is hard if not impossible to remember to go back and do all of those little, but important tasks. Also if you have a checklist, you can easily delegate other tasks to people and keep track of them in one place.</p>
    <p class="indent">b. By following through until the end - you'll ensure that your event is a success from start to finish. Although you'll have put in some more work up front as opposed to just 'winging it' your investment will pay dividends. While someone else is scrambling around at the last minute to find a new venue because they overlooked a key detail that is a show stopper, or wondering why less people than expected showed up, you will rest easy knowing that your event is at the right venue, that all of the details have been accounted for and that you'll be relaxing and enjoying the event, rather than running around putting out fires.</p>
    <h4 class="section" style="text-decoration:none">Congrats!</h4>
    <p>You're on your way to planning an event that people will talk about for years and in a good way. You won't have your name tied to the event where the room was too small or the food was cold, and you can be confident that you've planned a great event by selecting the best possible venue.</p>
    <p>To recap</p>
    <p>1. Know the type of event you're planning<br>2. Don't just know your event - know your audience<br>3. Ask the venue the right questions<br>4. Plan the food and drinks - that's why everyone is coming in the first place<br>5. Lastly, Don't take anything for granted</p>
    <p>P.S. Be on the lookout for our event planning checklist that I'll be sending you in a couple days!</p>
    <p>A special thanks to Mara Quill, Dean Harlow, Nina Vaskell and Ash Doyle who helped put this guide together. Together they have been planning events for over a decade that have brought our community closer together.</p>
  </div>
  <div class="page-number">6</div><div class="corner-name">TR</div>
</article>

<!-- Page 7 -->
<article class="page row-bottom" style="left:611px">
  <header class="page-header"><svg class="header-wave"><use href="#wave"/></svg><div class="brand-name"><span class="mark"></span>Tallow Roost</div></header>
  <div class="page-body checklist">
    <h2 class="section" style="text-decoration:none;font-size:5.4px;margin-top:5px">Event Planning Checklist</h2>
    <p>Every event is unique, but this should help serve as a general checklist for most events.</p>
    <h4>As Early As Possible</h4>
    <ul><li>Number of guests</li><li>Date(s) for the event (Factor in your speakers schedule if needed)</li><li>General location</li><li>Type of venue (Casual vs Formal, Indoor vs Outdoor, Quiet private room vs Open area)</li><li>Develop an initial budget</li><li>Book Your Venue</li><li>Go to www.tallowroost.com to compare venues.</li></ul>
    <h4>Confirm Event Details</h4>
    <ul><li>Confirm your speaker(s) and any remaining marketing details with them</li><li>Coordinate key details with the venue like what will be served, timing, etc.</li><li>Set up event on social media and/or a ticketing site if using that platform</li></ul>
    <h4>Notify Your Guests</h4>
    <ul><li>Email your guests</li><li>Post the event to social media and group pages</li><li>Send out more formal invites if necessary</li></ul>
    <h4>Coordinate With Vendors</h4>
    <ul><li>Photographer</li><li>Food</li><li>Beverages</li><li>Music (DJ, Band, etc)</li><li>Audio/Visual Support</li><li>Decorations</li><li>Glassware/attendee gifts</li><li>Child Care</li><li>Tables and chairs</li><li>Linens</li></ul>
    <h4>Military Specific Considerations</h4>
    <ul><li>Identify the Color Guard</li><li>Coordinate with the units band</li><li>Coordinate with the protocol office if senior leaders are attending</li><li>Coordinate with PAO</li><li>Conduct any necessary legal reviews</li></ul>
  </div>
  <div class="page-number">7</div><div class="corner-name">TR</div>
</article>

<!-- Page 8 -->
<article class="page row-bottom" style="left:802px">
  <header class="page-header"><svg class="header-wave"><use href="#wave"/></svg><div class="brand-name"><span class="mark"></span>Tallow Roost</div></header>
  <div class="page-body checklist">
    <h4 style="margin-top:5px">Execution</h4>
    <ul><li>Check up on marketing and ticket sales/attendees and see if you need to adjust anything</li><li>Reconfirm budget based off of the updated number of guests</li><li>Organize speaker gifts</li><li>VIP travel coordination</li></ul>
    <h4>1 Week Prior to the Event</h4>
    <ul><li>Re-confirm the venue and update them on any changes to guest count</li><li>Re-confirm all speakers</li><li>Re-confirm all vendors</li><li>Ensure the budget is matching up</li><li>Print necessary materials (programs, name tags, name tents, etc)</li><li>Contact attendees with the update agenda and key information like when and where the event starts, attire, if they should bring their ticket, parking instructions, directions, special instructions, etc.</li><li>Develop the script and confirm the bios match up and all participants understand and have practiced their part (if necessary)</li><li>Conduct venue walk through</li></ul>
    <h4>Day Before</h4>
    <ul><li>Re-confirm all details</li></ul>
    <h4>After</h4>
    <ul><li>Coordinate payment if necessary</li><li>Facilitate lost and found between the venue and guests if necessary</li></ul>
  </div>
  <div class="page-number">8</div><div class="corner-name">TR</div>
</article>

<!-- Back cover -->
<section class="cover cover-back">
  <div class="cover-logo" style="left:30px;top:126px"><span class="mark"></span>Tallow Roost</div>
  <svg class="cover-band" style="top:160px" width="180" height="76" viewBox="0 0 180 76" aria-hidden="true">
    <path d="M0 18 C60 4 120 10 180 0 L180 76 L0 76 Z" fill="var(--brand)"/>
    <path d="M0 13 C60 0 120 6 180 -4" fill="none" stroke="var(--brand)" stroke-width="0.6"/>
  </svg>
</section>

</body>
</html>
```